Pyschiatry Experts need Marketing Campaign

Ad(s) developed for print advertising sharing our purpose and services, highlighting our medical care providers. Must be welcoming and inviting while displaying a high level of professionalism expected from a physician's office.

Target Market(s)

Local community

Industry/Entity Type

Psychiatry (Healthcare)

Requirements
Must have
• Staff pictures, 'Medication Management Experts', 'Prompt Appointments', 'ADD/ADHD, Bipolar Disorder, Depression, Anxiety, Schizophrenia, Grief Reaction and others' 'Virtual and In-Person Visits'
Nice to have
• Address: 412 E Marlowe Coeur d'Alene Phone (208)555-7813 website: BrightKestrel.example Hours: Mon - Thur 7am - 6pm

```html
<!DOCTYPE html>
<html lang="en">
<head>
<meta charset="utf-8">
<title>Bright Kestrel Health – Medication Management Ads</title>
<link rel="stylesheet" href="https://fonts.googleapis.com/css2?family=Poppins:ital,wght@0,400;0,500;0,600;0,700;0,800;1,400&display=swap">
<style>
  :root{
    --board:#2a2a2a;
    --board-light:#3a3a3a;
    --teal:#13a08f;
    --teal-deep:#0c8a7c;
    --cyan:#2fe0dc;
    --green:#7fcf3f;
    --ink-teal:#179684;
    --white:#ffffff;
  }
  *{box-sizing:border-box;margin:0;padding:0}
  html,body{width:1145px;height:1200px;overflow:hidden}
  body{
    background:radial-gradient(ellipse at 50% 20%,var(--board-light),var(--board) 70%);
    font-family:"Poppins",sans-serif;
    position:relative;
  }
  .ad{
    position:absolute;width:478px;height:478px;overflow:hidden;
    box-shadow:0 14px 30px rgba(0,0,0,.55);
    color:var(--white);
  }
  .ad--a{left:59px;top:104px;background:radial-gradient(circle at 60% 45%,#3fe6dc 0%,var(--teal) 55%,var(--teal-deep) 100%)}
  .ad--b{left:595px;top:104px;background:radial-gradient(circle at 35% 40%,#d6f5a8 0%,var(--green) 45%,var(--teal) 100%)}
  .ad--c{left:59px;top:629px;background:radial-gradient(circle at 30% 55%,#3fe6dc 0%,var(--teal) 50%,var(--green) 100%)}
  .ad--d{left:595px;top:629px;background:radial-gradient(circle at 25% 55%,#45e3d6 0%,var(--teal) 55%,#2fae7a 100%)}

  .ad__photo{position:absolute;bottom:53px}
  .ad__curve{position:absolute;left:0;top:0;width:478px;height:478px}
  .ad--a .ad__photo{left:0;width:290px;height:382px;border-radius:130px 150px 0 0;background:linear-gradient(180deg,rgba(80,50,40,.55) 0%,rgba(20,20,20,.85) 45%,#111 100%)}
  .ad--b .ad__photo{left:0;width:300px;height:378px;border-radius:130px 150px 0 0;background:linear-gradient(180deg,rgba(230,200,180,.6) 0%,rgba(200,220,245,.95) 45%,#c9dcf3 100%)}
  .ad--c .ad__photo{left:210px;width:268px;height:380px;border-radius:150px 90px 0 0;background:linear-gradient(180deg,rgba(220,200,190,.6) 0%,rgba(30,30,35,.9) 45%,#111 100%)}
  .ad--d .ad__photo{left:200px;width:278px;height:378px;border-radius:150px 90px 0 0;background:linear-gradient(180deg,rgba(220,170,150,.55) 0%,rgba(70,95,130,.95) 45%,#44607f 100%)}

  .brand{position:absolute;top:10px;width:200px;text-align:center;color:var(--ink-teal)}
  .ad--a .brand,.ad--b .brand{left:261px}
  .ad--c .brand,.ad--d .brand{left:16px}
  .brand__dot{display:block;width:58px;height:58px;border-radius:50%;background:var(--ink-teal);margin:0 auto 8px}
  .brand__name{font-weight:600;font-size:19px;line-height:22px;letter-spacing:.5px}

  .headline{position:absolute;top:164px;font-weight:800;line-height:29px;font-size:34px;letter-spacing:-.3px;text-shadow:0 2px 4px rgba(0,0,0,.15)}
  .headline span{display:block}
  .headline .big{font-size:44px;line-height:40px}
  .ad--a .headline,.ad--b .headline{right:16px;text-align:right}
  .ad--c .headline,.ad--d .headline{left:18px;text-align:left}

  .pill{position:absolute;top:270px;height:24px;border:2px solid var(--cyan);font-weight:700;font-size:12.5px;line-height:20px;letter-spacing:.2px}
  .ad--a .pill,.ad--b .pill{left:290px;right:-4px;border-radius:14px 0 0 14px;padding-left:10px}
  .ad--c .pill,.ad--d .pill{left:-4px;width:190px;border-radius:0 14px 14px 0;padding-left:21px}

  .conditions{position:absolute;top:306px;list-style:none;font-style:italic;font-size:12.5px;line-height:15px}
  .ad--a .conditions,.ad--b .conditions{right:16px;text-align:right}
  .ad--a .conditions li::after,.ad--b .conditions li::after{content:"•";color:var(--cyan);margin-left:7px}
  .ad--a .conditions li.more,.ad--b .conditions li.more{margin-right:15px}
  .ad--a .conditions li.more::after,.ad--b .conditions li.more::after{content:none}
  .ad--c .conditions,.ad--d .conditions{left:17px}
  .ad--c .conditions li::before,.ad--d .conditions li::before{content:"•";color:var(--cyan);margin-right:6px}
  .ad--c .conditions li.more,.ad--d .conditions li.more{margin-left:10px}
  .ad--c .conditions li.more::before,.ad--d .conditions li.more::before{content:none}

  .contact{position:absolute;left:0;bottom:0;width:478px;height:53px;background:var(--white);color:var(--ink-teal);font-weight:500}
  .contact__item{position:absolute;display:flex;align-items:center;gap:5px;white-space:nowrap}
  .contact__icon{width:15px;height:15px;flex:none}
  .contact__address{font-size:12px;line-height:13px}
  .contact__phone{font-size:14px}
  .contact__web{font-size:11.5px}
  .visits{position:absolute;top:8px;height:35px;font-weight:800;color:var(--white);text-align:right;line-height:12px;padding-top:6px}
  .visits b{display:block;font-size:12px}
  .visits small{display:block;font-size:9px;font-weight:800}
  .ad--a .visits,.ad--b .visits{right:0;width:114px;border-radius:18px 0 0 18px;padding-right:9px}
  .ad--a .visits{background:var(--teal)}
  .ad--b .visits{background:linear-gradient(90deg,var(--teal),var(--green))}
  .ad--c .visits,.ad--d .visits{left:0;width:114px;border-radius:0 18px 18px 0;text-align:left;padding-left:10px}
  .ad--c .visits{background:var(--green)}
  .ad--d .visits{background:var(--teal)}
</style>
</head>
<body>

<article class="ad ad--a">
  <div class="ad__photo" role="img" aria-label="Portrait photo of a smiling provider with shoulder-length dark hair in a black top"></div>
  <svg class="ad__curve" viewBox="0 0 478 478"><path d="M172 0 C185 95 260 155 350 153 C410 152 450 135 478 118 V0 Z" fill="#fff"/></svg>
  <div class="brand"><span class="brand__dot"></span><span class="brand__name">BRIGHT KESTREL<br>HEALTH</span></div>
  <h2 class="headline"><span>MEDICATION</span><span>MANAGEMENT</span><span class="big">EXPERTS</span></h2>
  <p class="pill">PROMPT APPOINTMENTS</p>
  <ul class="conditions"><li>ADD/ADHD</li><li>Bipolar Disorder</li><li>Depression</li><li>Anxiety</li><li>Schizophrenia</li><li>Grief Reaction</li><li class="more">and others</li></ul>
  <footer class="contact">
    <div class="contact__item contact__address" style="left:10px;top:13px">
      <svg class="contact__icon" viewBox="0 0 16 16"><path d="M8 1a5 5 0 0 0-5 5c0 4 5 9 5 9s5-5 5-9a5 5 0 0 0-5-5z" fill="currentColor"/><circle cx="8" cy="6" r="2" fill="#fff"/></svg>
      <span>412 E Marlowe<br>Coeur d'Alene</span></div>
    <div class="contact__item contact__phone" style="left:165px;top:7px">
      <svg class="contact__icon" viewBox="0 0 16 16"><circle cx="8" cy="8" r="8" fill="currentColor"/><path d="M5 4.5l1.5-.5 1 2-1 .8a5 5 0 0 0 2.7 2.7l.8-1 2 1-.5 1.5C9 11.5 4.5 7 5 4.5z" fill="#fff"/></svg>
      <span>(208)555-7813</span></div>
    <div class="contact__item contact__web" style="left:165px;top:29px">
      <svg class="contact__icon" viewBox="0 0 16 16" fill="none" stroke="currentColor" stroke-width="1.4"><circle cx="8" cy="8" r="6.5"/><ellipse cx="8" cy="8" rx="3" ry="6.5"/><path d="M1.5 8h13M2.5 5h11M2.5 11h11"/></svg>
      <span>www.BrightKestrel.example</span></div>
    <div class="visits"><b>VIRTUAL AND</b><small>IN-PERSON VISITS</small></div>
  </footer>
</article>

<article class="ad ad--b">
  <div class="ad__photo" role="img" aria-label="Portrait photo of a smiling provider in a light blue shirt"></div>
  <svg class="ad__curve" viewBox="0 0 478 478"><path d="M172 0 C185 95 260 155 350 153 C410 152 450 135 478 118 V0 Z" fill="#fff"/></svg>
  <div class="brand"><span class="brand__dot"></span><span class="brand__name">BRIGHT KESTREL<br>HEALTH</span></div>
  <h2 class="headline"><span>MEDICATION</span><span>MANAGEMENT</span><span class="big">EXPERTS</span></h2>
  <p class="pill">PROMPT APPOINTMENTS</p>
  <ul class="conditions"><li>ADD/ADHD</li><li>Bipolar Disorder</li><li>Depression</li><li>Anxiety</li><li>Schizophrenia</li><li>Grief Reaction</li><li class="more">and others</li></ul>
  <footer class="contact">
    <div class="contact__item contact__address" style="left:10px;top:13px">
      <svg class="contact__icon" viewBox="0 0 16 16"><path d="M8 1a5 5 0 0 0-5 5c0 4 5 9 5 9s5-5 5-9a5 5 0 0 0-5-5z" fill="var(--green)"/><circle cx="8" cy="6" r="2" fill="#fff"/></svg>
      <span>412 E Marlowe<br>Coeur d'Alene</span></div>
    <div class="contact__item contact__phone" style="left:165px;top:7px">
      <svg class="contact__icon" viewBox="0 0 16 16"><circle cx="8" cy="8" r="8" fill="var(--green)"/><path d="M5 4.5l1.5-.5 1 2-1 .8a5 5 0 0 0 2.7 2.7l.8-1 2 1-.5 1.5C9 11.5 4.5 7 5 4.5z" fill="#fff"/></svg>
      <span>(208)555-7813</span></div>
    <div class="contact__item contact__web" style="left:165px;top:29px">
      <svg class="contact__icon" viewBox="0 0 16 16" fill="none" stroke="var(--green)" stroke-width="1.4"><circle cx="8" cy="8" r="6.5"/><ellipse cx="8" cy="8" rx="3" ry="6.5"/><path d="M1.5 8h13M2.5 5h11M2.5 11h11"/></svg>
      <span>www.BrightKestrel.example</span></div>
    <div class="visits"><b>VIRTUAL AND</b><small>IN-PERSON VISITS</small></div>
  </footer>
</article>

<article class="ad ad--c">
  <div class="ad__photo" role="img" aria-label="Portrait photo of a smiling senior provider with silver hair in a black top"></div>
  <svg class="ad__curve" viewBox="0 0 478 478"><path d="M0 0 H305 C290 95 220 155 130 153 C70 152 30 145 0 137 Z" fill="#fff"/></svg>
  <div class="brand"><span class="brand__dot"></span><span class="brand__name">BRIGHT KESTREL<br>HEALTH</span></div>
  <h2 class="headline"><span>MEDICATION</span><span>MANAGEMENT</span><span class="big">EXPERTS</span></h2>
  <p class="pill">PROMPT APPOINTMENTS</p>
  <ul class="conditions"><li>ADD/ADHD</li><li>Bipolar Disorder</li><li>Depression</li><li>Anxiety</li><li>Schizophrenia</li><li>Grief Reaction</li><li class="more">and others</li></ul>
  <footer class="contact">
    <div class="visits"><b>VIRTUAL AND</b><small>IN-PERSON VISITS</small></div>
    <div class="contact__item contact__phone" style="right:158px;top:7px;flex-direction:row-reverse">
      <svg class="contact__icon" viewBox="0 0 16 16"><circle cx="8" cy="8" r="8" fill="var(--green)"/><path d="M5 4.5l1.5-.5 1 2-1 .8a5 5 0 0 0 2.7 2.7l.8-1 2 1-.5 1.5C9 11.5 4.5 7 5 4.5z" fill="#fff"/></svg>
      <span>(208)555-7813</span></div>
    <div class="contact__item contact__web" style="right:158px;top:29px;flex-direction:row-reverse">
      <svg class="contact__icon" viewBox="0 0 16 16" fill="none" stroke="var(--green)" stroke-width="1.4"><circle cx="8" cy="8" r="6.5"/><ellipse cx="8" cy="8" rx="3" ry="6.5"/><path d="M1.5 8h13M2.5 5h11M2.5 11h11"/></svg>
      <span>www.BrightKestrel.example</span></div>
    <div class="contact__item contact__address" style="right:10px;top:13px;flex-direction:row-reverse;text-align:right">
      <svg class="contact__icon" viewBox="0 0 16 16"><path d="M8 1a5 5 0 0 0-5 5c0 4 5 9 5 9s5-5 5-9a5 5 0 0 0-5-5z" fill="var(--green)"/><circle cx="8" cy="6" r="2" fill="#fff"/></svg>
      <span>412 E Marlowe<br>Coeur d'Alene</span></div>
  </footer>
</article>

<article class="ad ad--d">
  <div class="ad__photo" role="img" aria-label="Portrait photo of a bearded provider in a navy button-up shirt"></div>
  <svg class="ad__curve" viewBox="0 0 478 478"><path d="M0 0 H305 C290 95 220 155 130 153 C70 152 30 145 0 137 Z" fill="#fff"/></svg>
  <div class="brand"><span class="brand__dot"></span><span class="brand__name">BRIGHT KESTREL<br>HEALTH</span></div>
  <h2 class="headline"><span>MEDICATION</span><span>MANAGEMENT</span><span class="big">EXPERTS</span></h2>
  <p class="pill">PROMPT APPOINTMENTS</p>
  <ul class="conditions"><li>ADD/ADHD</li><li>Bipolar Disorder</li><li>Depression</li><li>Anxiety</li><li>Schizophrenia</li><li>Grief Reaction</li><li class="more">and others</li></ul>
  <footer class="contact">
    <div class="visits"><b>VIRTUAL AND</b><small>IN-PERSON VISITS</small></div>
    <div class="contact__item contact__phone" style="right:158px;top:7px;flex-direction:row-reverse">
      <svg class="contact__icon" viewBox="0 0 16 16"><circle cx="8" cy="8" r="8" fill="currentColor"/><path d="M5 4.5l1.5-.5 1 2-1 .8a5 5 0 0 0 2.7 2.7l.8-1 2 1-.5 1.5C9 11.5 4.5 7 5 4.5z" fill="#fff"/></svg>
      <span>(208)555-7813</span></div>
    <div class="contact__item contact__web" style="right:158px;top:29px;flex-direction:row-reverse">
      <svg class="contact__icon" viewBox="0 0 16 16" fill="none" stroke="currentColor" stroke-width="1.4"><circle cx="8" cy="8" r="6.5"/><ellipse cx="8" cy="8" rx="3" ry="6.5"/><path d="M1.5 8h13M2.5 5h11M2.5 11h11"/></svg>
      <span>www.BrightKestrel.example</span></div>
    <div class="contact__item contact__address" style="right:10px;top:13px;flex-direction:row-reverse;text-align:right">
      <svg class="contact__icon" viewBox="0 0 16 16"><path d="M8 1a5 5 0 0 0-5 5c0 4 5 9 5 9s5-5 5-9a5 5 0 0 0-5-5z" fill="currentColor"/><circle cx="8" cy="6" r="2" fill="#fff"/></svg>
      <span>412 E Marlowe<br>Coeur d'Alene</span></div>
  </footer>
</article>

</body>
</html>
```